Business Card Design Project

I am a psychotherapist, counselor and expressive arts therapist (means I use every art form imaginable in the service of healing). I'm just starting out in private practice in San Francisco, CA. I work with individual adults, children and families. I'd like the card to mirror the simplicity and color palate of my website. I also would love if there is a symbol, image of fire, flame or spark (that is warming, not frightening).

Check out my website: www.lorabecketmft.com

I want the cards to be printed in letter press so please keep that in mind!

Target Market(s)

Upper Middle Class Adults who are progressively minded, artistic or artists, open to psychotherapy, interested in health & healing.

Industry/Entity Type

Business

Requirements
Must have
• Text to be included:

Lora Becket
Counseling, Psychotherapy & Expressive Arts

2914 Alderwood Avenue, Suite D
San Francisco, CA 94127
p. 415.206.3791
lorajanebecket@meadowpost.net

www.lorabecketmft.com

MFT License Number 48671

It's OK to abbreviate Number to # or Street to St., etc.

Must be compatible with letter press printing.
Nice to have
• I don't have a logo. I don't expect designers to necessarily create one for me, but if someone comes up with a simple image (see above about flame), that would be great. I don't have much of a budget now, but expect that to change in the next year or so and then could buy a logo for my website, future letterhead, etc.

```html
<!DOCTYPE html>
<html lang="en">
<head>
<meta charset="utf-8">
<title>Lora Becket – Business Card</title>
<link href="https://fonts.googleapis.com/css2?family=Exo+2:wght@500;600;700&display=swap" rel="stylesheet">
<style>
  :root {
    --backdrop: #e4e4e4;
    --card: #ffffff;
    --accent: #e23a5c;
    --accent-soft: #ec6f88;
    --ink: #4a4a4a;
  }
  * { box-sizing: border-box; margin: 0; padding: 0; }
  html, body {
    width: 1200px; height: 861px; overflow: hidden;
    background: var(--backdrop);
    font-family: "Exo 2", sans-serif;
  }
  .card {
    position: absolute; left: 150px; top: 173px;
    width: 900px; height: 514px;
    background: var(--card);
    box-shadow: 0 10px 30px rgba(0,0,0,0.15);
    overflow: hidden;
  }
  .stripes { position: absolute; left: 0; width: 900px; height: 50px; }
  .stripes--top { top: 28px; }
  .stripes--bottom { top: 440px; }
  .stripes line { stroke: var(--accent); stroke-width: 3; }

  .identity { position: absolute; left: 0; top: 170px; }
  .identity__name {
    margin-left: 48px;
    font-size: 40px; font-weight: 700; letter-spacing: 0.5px;
    color: var(--accent); text-transform: uppercase;
  }
  .identity__ribbon {
    position: relative; margin-top: 12px;
    width: 440px; height: 40px;
  }
  .identity__ribbon svg { position: absolute; inset: 0; }
  .identity__ribbon polygon { fill: var(--accent); }
  .identity__tagline {
    position: relative; line-height: 40px; padding-left: 48px;
    font-size: 15px; font-weight: 600; color: #fff; text-transform: uppercase;
  }

  .contacts { position: absolute; left: 520px; top: 148px; width: 380px; list-style: none; }
  .contacts__item {
    position: relative; display: flex; align-items: flex-end;
    padding: 0 0 6px 0; margin-bottom: 16px;
    border-bottom: 2px solid var(--accent);
    font-size: 18px; font-weight: 600; color: var(--ink);
    margin-right: 20px;
  }
  .contacts__icon { flex: none; width: 26px; height: 26px; margin-right: 12px; }
  .contacts__icon circle { fill: var(--accent); }
  .contacts__icon .glyph { fill: #fff; stroke: none; }
  .contacts__icon .glyph-line { fill: none; stroke: #fff; stroke-width: 1.8; }
  .contacts__text { line-height: 1.3; }
</style>
</head>
<body>
<main class="card">
  <svg class="stripes stripes--top" viewBox="0 0 900 50" aria-hidden="true">
    <line x1="0" y1="6" x2="900" y2="4"/>
    <line x1="0" y1="15" x2="900" y2="13"/>
    <line x1="0" y1="24" x2="900" y2="22"/>
    <line x1="0" y1="33" x2="900" y2="31"/>
    <line x1="0" y1="42" x2="900" y2="40"/>
  </svg>

  <section class="identity">
    <h1 class="identity__name">Lora Becket</h1>
    <div class="identity__ribbon">
      <svg viewBox="0 0 440 40" aria-hidden="true"><polygon points="0,0 428,0 440,20 428,40 0,40"/></svg>
      <p class="identity__tagline">Counseling, Psychotherapy &amp; Expressive Arts</p>
    </div>
  </section>

  <ul class="contacts">
    <li class="contacts__item">
      <svg class="contacts__icon" viewBox="0 0 26 26" aria-hidden="true"><circle cx="13" cy="13" r="13"/><path class="glyph" d="M13 6 L20 12 H18 V19 H14.5 V15 H11.5 V19 H8 V12 H6 Z"/></svg>
      <span class="contacts__text">2914 Alderwood Avenue, Suite D<br>San Francisco, CA 94127</span>
    </li>
    <li class="contacts__item">
      <svg class="contacts__icon" viewBox="0 0 26 26" aria-hidden="true"><circle cx="13" cy="13" r="13"/><path class="glyph" d="M8 17 L10 19 L18 9 L16 7 Z"/></svg>
      <span class="contacts__text">415.206.3791</span>
    </li>
    <li class="contacts__item">
      <svg class="contacts__icon" viewBox="0 0 26 26" aria-hidden="true"><circle cx="13" cy="13" r="13"/><rect class="glyph-line" x="7" y="9" width="12" height="8"/><path class="glyph-line" d="M7 9 L13 14 L19 9"/></svg>
      <span class="contacts__text">lorajanebecket@meadowpost.net</span>
    </li>
    <li class="contacts__item">
      <svg class="contacts__icon" viewBox="0 0 26 26" aria-hidden="true"><circle cx="13" cy="13" r="13"/><rect class="glyph-line" x="7" y="7.5" width="12" height="8.5"/><path class="glyph-line" d="M13 16 V19 M10 19.5 H16"/></svg>
      <span class="contacts__text">www.lorabecketmft.com</span>
    </li>
    <li class="contacts__item">
      <svg class="contacts__icon" viewBox="0 0 26 26" aria-hidden="true"><circle cx="13" cy="13" r="13"/><rect class="glyph-line" x="6.5" y="8" width="13" height="10" rx="1"/><circle class="glyph" cx="11" cy="13" r="2"/><path class="glyph-line" d="M14.5 11.5 H17.5 M14.5 14.5 H17.5"/></svg>
      <span class="contacts__text">MFT License Number 48671</span>
    </li>
  </ul>

  <svg class="stripes stripes--bottom" viewBox="0 0 900 50" aria-hidden="true">
    <line x1="0" y1="4" x2="900" y2="8"/>
    <line x1="0" y1="13" x2="900" y2="17"/>
    <line x1="0" y1="22" x2="900" y2="26"/>
    <line x1="0" y1="31" x2="900" y2="35"/>
    <line x1="0" y1="40" x2="900" y2="44"/>
  </svg>
</main>
</body>
</html>
```